Financial Services Company power point theme design

We need a PowerPoint theme designed for client presentations and company orientations. We do like modern designs using blue colors. attached is our logos the logo colors may change as needed to fit the theme. Landscape 16: 9 is acceptable

Industry/Entity Type

Financial Service

Colors

Designer to choose colors to be used in the design.

```html
<!DOCTYPE html>
<html lang="en">
<head>
<meta charset="utf-8">
<title>Keystone Ridge Financial – Presentation Theme</title>
<link href="https://fonts.googleapis.com/css2?family=Oswald:wght@500;600&family=Lato:wght@400;700&display=swap" rel="stylesheet">
<style>
:root{
  --navy:#111c36;
  --blue:#1f3766;
  --mid:#3a5386;
  --light:#f3f3f5;
  --grey:#e3e4e8;
  --bar:#c9cad0;
  --text:#3c4152;
  --white:#ffffff;
}
*{margin:0;padding:0;box-sizing:border-box}
html,body{width:1200px;height:1200px;overflow:hidden;background:var(--white)}
body{position:relative;font-family:"Lato",sans-serif;color:var(--text)}
.slide{position:absolute;overflow:hidden;background:var(--light)}
.slide > *{position:absolute}
.dark{background:var(--navy)}
.shape{left:0;top:0}
.heading{font-family:"Oswald",sans-serif;font-weight:600;color:var(--navy);letter-spacing:.16em;text-transform:uppercase;white-space:nowrap}
.title{font-family:"Oswald",sans-serif;font-weight:500;color:var(--white);text-transform:uppercase;font-size:21px;line-height:1.55;letter-spacing:.02em;text-align:right}
.subtitle{color:var(--white);font-size:12px;letter-spacing:.06em;text-align:right}
.body{font-size:6.6px;line-height:1.3}
.body.light{color:#c9cedb}
.body.center{text-align:center}
.body.right{text-align:right}
.body.justify{text-align:justify}
.bar-mark{height:8px;background:var(--bar)}
.underline{height:2px;background:var(--navy)}
.photo-sea{background:linear-gradient(180deg,#d3d1cc 0%,#a9b3b7 48%,#3a5966 54%,#1b3442 100%)}
.photo-person{background:linear-gradient(180deg,#d6d8dc,#8c93a3)}
.photo-dark{background:radial-gradient(circle at 45% 45%,#4a4f5c 0%,#1a1d26 55%,#0e111a 100%)}
.photo-building{background:linear-gradient(135deg,#f0f0f2,#cfd1d6)}
.photo-pyramid{background:linear-gradient(160deg,#e8e9ec,#a5a9b1)}
.brand{font-family:"Lato",sans-serif;font-weight:700;color:var(--navy);text-transform:uppercase;letter-spacing:.06em;white-space:nowrap;display:flex;align-items:center;gap:5px}
.brand .dot{width:9px;height:9px;background:currentColor;display:inline-block}
.brand.white{color:var(--white)}
.team-name{font-size:8.5px;font-weight:700;text-align:center;width:80px}
.item-title{font-size:10px;font-weight:700;color:var(--navy)}
.item-sub{font-size:8.5px;color:var(--text)}
.caption{position:absolute;left:17px;top:1160px;font-size:29px;color:#111;font-family:"Lato",sans-serif}
table.data{border-collapse:collapse;font-size:6.6px;width:171px}
table.data th{background:var(--navy);color:var(--white);font-family:"Oswald",sans-serif;font-weight:600;text-align:left;padding:2px 5px;text-transform:uppercase}
table.data td{padding:2px 5px;color:var(--text)}
table.data tr:nth-child(odd) td{background:#c9cad0}
table.data tr:nth-child(even) td{background:#eeeef0}
</style>
</head>
<body>

<!-- Row 1 -->
<section class="slide" style="left:0;top:0;width:394px;height:226px">
  <svg class="shape" width="394" height="226"><polygon points="304,0 394,0 394,226 196,226" fill="#111c36"/>
    <line x1="107" y1="0" x2="107" y2="24" stroke="#111c36"/><line x1="107" y1="208" x2="107" y2="226" stroke="#111c36"/>
    <polygon points="107,24 199,116 107,208 15,116" fill="#fff" stroke="#111c36" stroke-width="1.2"/>
    <line x1="20" y1="128" x2="92" y2="200" stroke="#111c36" stroke-width="6"/></svg>
  <div class="brand" style="left:50px;top:94px;font-size:10px;flex-direction:column;gap:4px"><span class="dot"></span><span>Keystone Ridge</span><span>Financial LLC.</span></div>
  <div class="title" style="right:24px;top:60px">Your Title<br>Text Here</div>
  <div class="subtitle" style="right:24px;top:130px">Subtitle text here</div>
  <p class="body light right" style="right:24px;top:178px;width:130px">Lorem ipsum dolor sit amet, quem prompta forensibus ei has, has saepe eloquentiam at.</p>
</section>

<section class="slide" style="left:394px;top:0;width:409px;height:226px">
  <div class="dark" style="left:0;top:0;width:186px;height:226px"></div>
  <div class="title" style="right:247px;top:22px">Your Title<br>Text Here</div>
  <div class="subtitle" style="right:247px;top:93px">Subtitle text here</div>
  <p class="body light right" style="right:247px;top:172px;width:130px">Lorem ipsum dolor sit amet, quem prompta forensibus ei has, has saepe eloquentiam at.</p>
  <div class="photo-building" role="img" aria-label="Soft light architectural photo of a modern building" style="left:186px;top:0;width:223px;height:226px"></div>
  <div class="brand" style="left:220px;top:70px;font-size:15px"><span class="dot"></span>Keystone Ridge</div>
  <div class="brand" style="left:200px;top:146px;font-size:6px;gap:14px"><span>Home Loans</span><span>Insurance Agency</span><span>Financial LLC.</span></div>
</section>

<section class="slide" style="left:803px;top:0;width:397px;height:226px">
  <p class="body justify" style="left:66px;top:42px;width:192px">Lorem ipsum dolor sit amet, quem prompta forensibus ei has, has saepe eloquentiam at. Enim consulatu percipitur ut nec, est fugit iudicabit te, alia consulatu an ius. Eu est numquam ancillae mediocritatem, habemus recteque no ius, mei eu possit conceptam.</p>
  <p class="body" style="left:32px;top:135px;width:205px">In mea aeque viderer deseruisse. Erant libris te eum, dolorum disputationi ne eum. Doming vocent facilisi vis an, vim perpetua dissentias temporibus eu, partem recteque sea ex. No sed suas tantas, noster tincidunt an vix. Sed dicunt dignissim honestatis te, vidit omnis falli at has.</p>
  <div class="brand" style="right:14px;top:22px;font-size:10px"><span class="dot"></span>Keystone Ridge</div>
  <div class="bar-mark" style="left:284px;top:84px;width:18px"></div>
  <div class="heading" style="left:302px;top:74px;font-size:17px">About Us</div>
  <div class="photo-sea" role="img" aria-label="Calm sea horizon photo" style="left:294px;top:108px;width:94px;height:95px"></div>
  <div class="photo-pyramid" role="img" aria-label="Glass pyramid architecture photo" style="left:250px;top:122px;width:85px;height:88px"></div>
</section>

<!-- Row 2 -->
<section class="slide" style="left:0;top:226px;width:394px;height:230px">
  <svg class="shape" width="394" height="230"><polygon points="0,0 145,0 108,230 0,230" fill="#111c36"/><polygon points="238,0 394,0 394,230 253,230" fill="#111c36"/></svg>
  <div class="heading" style="left:4px;top:16px;font-size:15px;color:var(--white)">Meet Our Team</div>
  <div class="photo-person" role="img" aria-label="Team member portrait" style="left:29px;top:61px;width:73px;height:71px"></div>
  <div class="photo-person" role="img" aria-label="Team member portrait" style="left:152px;top:61px;width:73px;height:71px"></div>
  <div class="photo-person" role="img" aria-label="Team member portrait" style="left:277px;top:61px;width:73px;height:71px"></div>
  <div class="team-name" style="left:26px;top:140px;color:var(--white)">Full Name</div>
  <div class="team-name" style="left:149px;top:140px;color:var(--navy)">Full Name</div>
  <div class="team-name" style="left:274px;top:140px;color:var(--white)">Full Name</div>
  <p class="body light center" style="left:28px;top:153px;width:76px">Lorem ipsum dolor sit amet, quem prompta forensibus ei has, has saepe eloquentiam at. Enim consulatu percipitur ut nec, est fugit iudicabit te.</p>
  <p class="body center" style="left:151px;top:153px;width:76px">Lorem ipsum dolor sit amet, quem prompta forensibus ei has, has saepe eloquentiam at. Enim consulatu percipitur ut nec, est fugit iudicabit te.</p>
  <p class="body light center" style="left:276px;top:153px;width:76px">Lorem ipsum dolor sit amet, quem prompta forensibus ei has, has saepe eloquentiam at. Enim consulatu percipitur ut nec, est fugit iudicabit te.</p>
</section>

<section class="slide" style="left:394px;top:226px;width:409px;height:230px">
  <div class="bar-mark" style="left:216px;top:40px;width:18px"></div>
  <div class="heading" style="left:84px;top:30px;font-size:19px">Our Profile</div>
  <div style="right:192px;top:84px;font-size:13px;color:#111">Name Here</div>
  <p class="body center" style="left:56px;top:128px;width:158px">Lorem ipsum dolor sit amet, quem prompta forensibus ei has, has saepe eloquentiam at. Enim consulatu percipitur ut nec, est fugit iudicabit te, alia consulatu an ius. Eu est numquam ancillae mediocritatem, habemus recteque no ius, mei eu possit conceptam. Pro at idque omittam, his ei quas phaedrum quaerendum.</p>
  <div class="photo-dark" role="img" aria-label="Dark studio portrait photo" style="left:237px;top:0;width:172px;height:230px"></div>
</section>

<section class="slide" style="left:803px;top:226px;width:397px;height:230px">
  <svg class="shape" width="397" height="230"><polygon points="0,0 55,0 0,40" fill="#111c36"/></svg>
  <div class="bar-mark" style="left:138px;top:34px;width:22px"></div>
  <div class="heading" style="left:160px;top:24px;font-size:17px">Contents</div>
  <div class="underline" style="left:200px;top:52px;width:32px"></div>
  <div class="brand" style="left:322px;top:22px;font-size:6px"><span class="dot" style="width:6px;height:6px"></span>Keystone</div>
  <svg class="shape" width="397" height="230" font-family="Oswald,sans-serif" font-size="10" fill="#fff" text-anchor="middle">
    <g fill="#1f3766">
      <rect x="37" y="80" width="18" height="18" transform="rotate(45 46 89)"/><rect x="37" y="126" width="18" height="18" transform="rotate(45 46 135)"/><rect x="37" y="173" width="18" height="18" transform="rotate(45 46 182)"/>
      <rect x="224" y="80" width="18" height="18" transform="rotate(45 233 89)"/><rect x="224" y="126" width="18" height="18" transform="rotate(45 233 135)"/><rect x="224" y="173" width="18" height="18" transform="rotate(45 233 182)"/>
    </g>
    <text x="46" y="93">1</text><text x="46" y="139">2</text><text x="46" y="186">3</text>
    <text x="233" y="93">4</text><text x="233" y="139">5</text><text x="233" y="186">6</text>
  </svg>
  <div style="left:72px;top:80px"><div class="item-title">Lorem ipsum</div><div class="item-sub">Lorem ipsum dolor sit amet</div></div>
  <div style="left:72px;top:126px"><div class="item-title">Lorem ipsum</div><div class="item-sub">Lorem ipsum dolor sit amet</div></div>
  <div style="left:72px;top:173px"><div class="item-title">Lorem ipsum</div><div class="item-sub">Lorem ipsum dolor sit amet</div></div>
  <div style="left:259px;top:80px"><div class="item-title">Lorem ipsum</div><div class="item-sub">Lorem ipsum dolor sit amet</div></div>
  <div style="left:259px;top:126px"><div class="item-title">Lorem ipsum</div><div class="item-sub">Lorem ipsum dolor sit amet</div></div>
  <div style="left:259px;top:173px"><div class="item-title">Lorem ipsum</div><div class="item-sub">Lorem ipsum dolor sit amet</div></div>
</section>

<!-- Row 3 -->
<section class="slide" style="left:0;top:456px;width:394px;height:230px">
  <svg class="shape" width="394" height="230"><polygon points="345,0 394,0 394,50" fill="#111c36"/></svg>
  <div class="photo-sea" role="img" aria-label="Blurred sea horizon photo" style="left:18px;top:33px;width:165px;height:165px"></div>
  <div class="heading" style="left:196px;top:34px;font-size:24px;letter-spacing:.12em">Left</div>
  <div class="heading" style="left:196px;top:68px;font-size:16px">Picture Slide</div>
  <div class="underline" style="left:229px;top:96px;width:60px"></div>
  <p class="body right" style="right:25px;top:138px;width:118px">Lorem ipsum dolor sit amet, quem prompta forensibus ei has, has saepe eloquentiam at. Enim consulatu percipitur ut nec, est fugit iudicabit te, alia consulatu an ius. Eu est numquam ancillae mediocritatem, habemus recteque no ius, mei eu possit conceptam.</p>
</section>

<section class="slide" style="left:394px;top:456px;width:409px;height:230px">
  <svg class="shape" width="409" height="230"><polygon points="0,170 0,230 50,230" fill="#111c36"/></svg>
  <div class="heading" style="left:0;width:409px;text-align:center;top:10px;font-size:24px;letter-spacing:.12em">Three</div>
  <div class="heading" style="left:0;width:409px;text-align:center;top:41px;font-size:16px">Picture Slide</div>
  <p class="body center" style="left:40px;top:71px;width:329px;white-space:nowrap">Lorem ipsum dolor sit amet, eu his ludus pertinax intellegebat, senserit postulant mnesarchum ut eos.</p>
  <div class="photo-sea" role="img" aria-label="Sea horizon photo" style="left:56px;top:96px;width:61px;height:62px"></div>
  <div class="photo-sea" role="img" aria-label="Sea horizon photo" style="left:174px;top:96px;width:61px;height:62px"></div>
  <div class="photo-sea" role="img" aria-label="Sea horizon photo" style="left:291px;top:96px;width:61px;height:62px"></div>
  <p class="body center" style="left:46px;top:166px;width:80px">Lorem ipsum dolor sit amet, quem prompta forensibus ei has, has saepe eloquentiam at.</p>
  <p class="body center" style="left:164px;top:166px;width:80px">Lorem ipsum dolor sit amet, quem prompta forensibus ei has, has saepe eloquentiam at.</p>
  <p class="body center" style="left:281px;top:166px;width:80px">Lorem ipsum dolor sit amet, quem prompta forensibus ei has, has saepe eloquentiam at.</p>
</section>

<section class="slide" style="left:803px;top:456px;width:397px;height:230px">
  <svg class="shape" width="397" height="230"><polygon points="0,0 50,0 0,55" fill="#111c36"/><polygon points="365,0 397,0 397,28" fill="#111c36"/></svg>
  <div class="bar-mark" style="left:142px;top:30px;width:16px"></div>
  <div class="heading" style="left:158px;top:20px;font-size:17px">List Slide</div>
  <div class="underline" style="left:200px;top:48px;width:32px"></div>
  <svg class="shape" width="397" height="230" font-family="Oswald,sans-serif" font-size="22" fill="#fff" text-anchor="middle">
    <circle cx="90" cy="91" r="19" fill="#111c36"/><circle cx="205" cy="91" r="19" fill="#111c36"/><circle cx="319" cy="91" r="19" fill="#111c36"/>
    <text x="90" y="99">1</text><text x="205" y="99">2</text><text x="319" y="99">3</text>
    <polyline points="142,88 153,118 142,162" fill="none" stroke="#111c36" stroke-width="2"/>
    <polyline points="256,88 267,118 256,162" fill="none" stroke="#111c36" stroke-width="2"/>
  </svg>
  <p class="body center" style="left:54px;top:126px;width:72px">Lorem ipsum dolor sit amet, quem prompta forensibus ei has, has saepe eloquentiam at. Enim consulatu percipitur ut nec, est fugit iudicabit te.</p>
  <p class="body center" style="left:169px;top:126px;width:72px">Lorem ipsum dolor sit amet, quem prompta forensibus ei has, has saepe eloquentiam at. Enim consulatu percipitur ut nec, est fugit iudicabit te.</p>
  <p class="body center" style="left:283px;top:126px;width:72px">Lorem ipsum dolor sit amet, quem prompta forensibus ei has, has saepe eloquentiam at. Enim consulatu percipitur ut nec, est fugit iudicabit te.</p>
</section>

<!-- Row 4 -->
<section class="slide" style="left:0;top:686px;width:394px;height:230px">
  <svg class="shape" width="394" height="230"><polygon points="0,0 35,0 0,28" fill="#111c36"/><polygon points="355,0 394,0 394,40" fill="#111c36"/></svg>
  <div class="bar-mark" style="left:125px;top:32px;width:16px"></div>
  <div class="heading" style="left:141px;top:22px;font-size:17px">List Slide</div>
  <div class="underline" style="left:193px;top:52px;width:32px"></div>
  <div class="dark" style="left:31px;top:75px;width:87px;height:129px"></div>
  <div class="dark" style="left:146px;top:75px;width:87px;height:129px"></div>
  <div class="dark" style="left:260px;top:75px;width:87px;height:129px"></div>
  <svg class="shape" width="394" height="230" font-family="Oswald,sans-serif" font-size="22" fill="#111c36" text-anchor="middle">
    <circle cx="75" cy="99" r="19" fill="#fff"/><circle cx="190" cy="99" r="19" fill="#fff"/><circle cx="304" cy="99" r="19" fill="#fff"/>
    <text x="75" y="107">1</text><text x="190" y="107">2</text><text x="304" y="107">3</text>
  </svg>
  <p class="body light center" style="left:37px;top:132px;width:75px">Lorem ipsum dolor sit amet, quem prompta forensibus ei has, has saepe eloquentiam at. Enim consulatu percipitur ut nec, est fugit iudicabit te.</p>
  <p class="body light center" style="left:152px;top:132px;width:75px">Lorem ipsum dolor sit amet, quem prompta forensibus ei has, has saepe eloquentiam at. Enim consulatu percipitur ut nec, est fugit iudicabit te.</p>
  <p class="body light center" style="left:266px;top:132px;width:75px">Lorem ipsum dolor sit amet, quem prompta forensibus ei has, has saepe eloquentiam at. Enim consulatu percipitur ut nec, est fugit iudicabit te.</p>
</section>

<section class="slide" style="left:394px;top:686px;width:409px;height:230px">
  <div class="dark" style="left:0;top:0;width:160px;height:230px"></div>
  <p class="body light justify" style="left:20px;top:97px;width:121px">Lorem ipsum dolor sit amet, quem prompta forensibus ei has, has saepe eloquentiam at. Enim consulatu percipitur ut nec, est fugit iudicabit te, alia consulatu an ius.</p>
  <div style="left:20px;top:156px;width:121px;height:1px;background:#4b5570"></div>
  <p class="body light justify" style="left:20px;top:172px;width:121px">Lorem ipsum dolor sit amet, quem prompta forensibus ei has, has saepe eloquentiam at. Enim consulatu percipitur ut nec, est fugit iudicabit te, alia consulatu an ius.</p>
  <div class="heading" style="right:27px;top:18px;font-size:17px">Data Slide</div>
  <div class="underline" style="right:27px;top:47px;width:32px"></div>
  <p class="body center" style="left:176px;top:65px;width:210px">Lorem ipsum dolor sit amet, quem prompta forensibus ei has, has saepe eloquentiam at. Enim consulatu percipitur ut nec, est fugit iudicabit te, alia consulatu an ius.</p>
  <svg class="shape" width="409" height="230" font-family="Oswald,sans-serif" font-size="5" fill="#3c4152" text-anchor="middle">
    <text x="290" y="110" font-size="7" font-weight="600" fill="#111c36">CHART TITLE</text>
    <g font-size="4.5"><rect x="252" y="116" width="3" height="3" fill="#111c36"/><text x="264" y="119">Series 1</text><rect x="280" y="116" width="3" height="3" fill="#1f3766"/><text x="292" y="119">Series 2</text><rect x="308" y="116" width="3" height="3" fill="#3a5386"/><text x="320" y="119">Series 3</text></g>
    <line x1="195" y1="200" x2="385" y2="200" stroke="#c9cad0"/>
    <g fill="#111c36"><rect x="208" y="146" width="5" height="54"/><rect x="255" y="144" width="5" height="56"/><rect x="302" y="154" width="5" height="46"/><rect x="348" y="145" width="5" height="55"/></g>
    <g fill="#3a5386"><rect x="215" y="169" width="5" height="31"/><rect x="262" y="160" width="5" height="40"/><rect x="309" y="177" width="5" height="23"/><rect x="355" y="159" width="5" height="41"/></g>
    <g fill="#1f3766"><rect x="222" y="176" width="5" height="24"/><rect x="269" y="176" width="5" height="24"/><rect x="316" y="164" width="5" height="36"/><rect x="362" y="137" width="5" height="63"/></g>
    <text x="218" y="209">CATEGORY 1</text><text x="265" y="209">CATEGORY 2</text><text x="312" y="209">CATEGORY 3</text><text x="358" y="209">CATEGORY 4</text>
  </svg>
</section>

<section class="slide" style="left:803px;top:686px;width:397px;height:230px">
  <svg class="shape" width="397" height="230"><polygon points="0,0 40,0 0,40" fill="#111c36"/></svg>
  <div class="heading" style="left:30px;top:18px;font-size:17px">Data Slide</div>
  <div class="underline" style="left:108px;top:45px;width:32px"></div>
  <p class="body" style="left:30px;top:57px;width:280px">Lorem ipsum dolor sit amet, quem prompta forensibus ei has, has saepe eloquentiam at. Enim consulatu percipitur ut nec, est fugit iudicabit te, alia consulatu an ius.</p>
  <p class="body justify" style="left:30px;top:104px;width:180px">Lorem ipsum dolor sit amet, quem prompta forensibus ei has, has saepe eloquentiam at. Enim consulatu percipitur ut nec, est fugit iudicabit te, alia consulatu an ius.</p>
  <div style="left:30px;top:150px;width:180px;height:1px;background:#c9cad0"></div>
  <p class="body justify" style="left:30px;top:170px;width:180px">Lorem ipsum dolor sit amet, quem prompta forensibus ei has, has saepe eloquentiam at. Enim consulatu percipitur ut nec, est fugit iudicabit te, alia consulatu an ius.</p>
  <svg class="shape" width="397" height="230" font-family="Oswald,sans-serif" text-anchor="middle">
    <text x="316" y="64" font-size="5.5" fill="#111c36">SALES</text>
    <path d="M322,130 L322,75 A55,55 0 1 1 286.6,172.1 Z" fill="#111c36"/>
    <path d="M322,130 L286.6,172.1 A55,55 0 0 1 270.3,111.2 Z" fill="#111c36" transform="translate(-6,1.5)"/>
    <path d="M322,130 L270.3,111.2 A55,55 0 0 1 298.8,80.2 Z" fill="#1f3766" transform="translate(-5,-4.5)"/>
    <path d="M322,130 L298.8,80.2 A55,55 0 0 1 322,75 Z" fill="#263356" transform="translate(-1.5,-6)"/>
    <g font-size="4.5" fill="#3c4152"><text x="282" y="213">■ 1st Qtr</text><text x="305" y="213">■ 2nd Qtr</text><text x="330" y="213">■ 3rd Qtr</text><text x="355" y="213">■ 4th Qtr</text></g>
  </svg>
</section>

<!-- Row 5 -->
<section class="slide" style="left:0;top:916px;width:394px;height:230px">
  <svg class="shape" width="394" height="230"><polygon points="0,0 30,0 0,22" fill="#111c36"/><polygon points="394,180 394,230 350,230" fill="#111c36"/></svg>
  <div class="heading" style="left:0;width:394px;text-align:center;top:15px;font-size:17px">Data Slide</div>
  <div class="underline" style="left:165px;top:43px;width:32px"></div>
  <p class="body center" style="left:14px;top:57px;width:366px;white-space:nowrap">Lorem ipsum dolor sit amet, eu his ludus pertinax intellegebat, senserit postulant mnesarchum ut eos.</p>
  <table class="data" style="left:13px;top:79px">
    <tr><th>No</th><th>Lorem</th><th>Ipsum</th><th>Dolor</th></tr>
    <tr><td>1</td><td>Stuff</td><td>Thing</td><td>Amount</td></tr>
    <tr><td>2</td><td>Stuff</td><td>Thing</td><td>Amount</td></tr>
    <tr><td>3</td><td>Stuff</td><td>Thing</td><td>Amount</td></tr>
    <tr><td>4</td><td>Stuff</td><td>Thing</td><td>Amount</td></tr>
  </table>
  <p class="body" style="left:204px;top:110px;width:142px">Lorem ipsum dolor sit amet, quem prompta forensibus ei has, has saepe eloquentiam at. Enim consulatu percipitur ut nec, est fugit iudicabit te, alia consulatu an ius.</p>
  <div class="heading" style="left:17px;top:166px;font-size:10px;letter-spacing:.3em">Results</div>
  <p class="body" style="left:17px;top:190px;width:330px">Lorem ipsum dolor sit amet, quem prompta forensibus ei has, has saepe eloquentiam at. Enim consulatu percipitur ut nec, est fugit iudicabit te, alia consulatu an ius.</p>
</section>

<section class="slide" style="left:394px;top:916px;width:249px;height:230px">
  <div class="heading" style="left:27px;top:16px;font-size:17px">Data Slide</div>
  <div class="underline" style="left:80px;top:44px;width:32px"></div>
  <p class="body" style="left:29px;top:57px;width:200px">Lorem ipsum dolor sit amet, quem prompta forensibus ei has, has saepe eloquentiam at. Enim consulatu percipitur ut nec, est fugit iudicabit te, alia consulatu an ius.</p>
  <svg class="shape" width="249" height="230" font-family="Oswald,sans-serif" font-size="4.5" fill="#3c4152" text-anchor="middle">
    <text x="124" y="101" font-size="7" font-weight="600" fill="#111c36">CHART TITLE</text>
    <text x="88" y="111">—● Series 1</text><text x="118" y="111">—● Series 2</text><text x="150" y="111">—● Series 3</text>
    <g text-anchor="end"><text x="39" y="123">6</text><text x="39" y="137">5</text><text x="39" y="151">4</text><text x="39" y="165">3</text><text x="39" y="179">2</text><text x="39" y="193">1</text><text x="39" y="207">0</text></g>
    <line x1="45" y1="205" x2="225" y2="205" stroke="#c9cad0"/><line x1="45" y1="120" x2="45" y2="205" stroke="#e0e0e4"/>
    <polyline points="61,146 105,170 149,156 195,143" fill="none" stroke="#1f3766"/>
    <polyline points="61,170 105,143 149,178 195,167" fill="none" stroke="#3c4152"/>
    <polyline points="61,177 105,177 149,165 195,136" fill="none" stroke="#9aa0ab"/>
    <text x="61" y="213">CATEGORY 1</text><text x="105" y="213">CATEGORY 2</text><text x="149" y="213">CATEGORY 3</text><text x="195" y="213">CATEGORY 4</text>
  </svg>
</section>

<section class="slide dark" style="left:643px;top:916px;width:557px;height:230px">
  <p class="body light justify" style="left:22px;top:19px;width:122px">Lorem ipsum dolor sit amet, quem prompta forensibus ei has, has saepe eloquentiam at. Enim consulatu percipitur ut nec, est fugit iudicabit te, alia consulatu an ius.</p>
  <div style="left:22px;top:78px;width:122px;height:1px;background:#4b5570"></div>
  <p class="body light justify" style="left:22px;top:94px;width:122px">Lorem ipsum dolor sit amet, quem prompta forensibus ei has, has saepe eloquentiam at. Enim consulatu percipitur ut nec, est fugit iudicabit te, alia consulatu an ius.</p>
  <div class="heading" style="left:180px;top:14px;font-size:26px;color:var(--white);letter-spacing:.01em">Thank You</div>
  <div class="brand white" style="right:18px;top:124px;font-size:12px;align-items:flex-start;gap:8px"><span class="dot" style="margin-top:3px"></span><span>Keystone Ridge<br>Financial LLC.</span></div>
  <p class="body light right" style="right:18px;top:166px;width:170px;font-size:7px">Insert contact person here:<br>Lorem ipsum dolor sit amet, quem prompta forensibus ei has, has saepe eloquentiam at. Enim consulatu percipitur ut nec, est fugit iudicabit te, alia consulatu an ius.</p>
</section>

<div class="caption">slideshow preview Keystone Ridge</div>

</body>
</html>
```